Thornwell Building Company - advertisement poster

I am looking to print some canvas signs to advertise my general contracting company, Thornwell Building Company. The sign will measure 6' long x 3' high so the size should match that ratio. I already have a logo icon, which is the Letter 'A' and some trees that I would like to incorporate, see attached. I would also like the to have the following information listed:
1) phone number: 472-318-6095
2) email: thornwellbuildingcompany@mailvistra.net
3) website: thornwellbuildingcompany.com
4) Lic#5386204
5) I want to use this text: "BUILD WITH THE T-CREW!"

The ad should be relatively simple and clean. Black and Green are my company colors. I am open to creative ideas!

Target Market(s)

People looking to renovate their homes

Industry/Entity Type

Construction

Colors
59FF00
82FF00
B8FF75
E3FFCB
F4FFEA

Requirements
Must have
• Must have my company logo
Should not have
• No photos or complex graphics

```html
<!DOCTYPE html>
<html lang="en">
<head>
<meta charset="utf-8">
<title>Thornwell Building Company – Banner Layouts</title>
<link href="https://fonts.googleapis.com/css2?family=Orbitron:wght@500;700;800;900&family=Exo+2:wght@300;400&display=swap" rel="stylesheet">
<style>
  :root {
    --page: #ffffff;
    --ink: #ffffff;
    --brand-green: #72b748;
    --band-dark: #121314;
    --band-mid: #1f1f20;
    --band-light: #333333;
    --display: "Orbitron", sans-serif;
    --body: "Exo 2", sans-serif;
  }
  * { margin: 0; padding: 0; box-sizing: border-box; }
  html, body {
    width: 1040px; height: 1200px; overflow: hidden;
    background: var(--page);
  }
  .sheet { position: relative; width: 1040px; height: 1200px; }

  .banner {
    position: absolute; left: 102px; width: 851px; height: 428px;
    overflow: hidden; color: var(--ink);
    background: var(--band-dark);
  }
  .banner--stacked { top: 115px; }
  .banner--split { top: 669px; }

  .banner__backdrop { position: absolute; inset: 0; width: 100%; height: 100%; }

  .headline {
    position: absolute; top: 44px; left: 0; right: 0;
    text-align: center;
    font-family: var(--display); font-weight: 900;
    font-size: 46px; letter-spacing: 1px; line-height: 1;
  }

  .brand {
    position: absolute; left: 0; right: 0;
    display: flex; align-items: center; justify-content: center; gap: 16px;
  }
  .banner--stacked .brand { top: 150px; }
  .banner--split .brand { top: 160px; }
  .brand__mark { width: 58px; height: 58px; background: var(--brand-green); flex: none; }
  .brand__name {
    font-family: var(--display); font-weight: 800; color: var(--ink);
    line-height: 1; text-align: left;
  }
  .brand__primary { display: block; font-size: 44px; letter-spacing: 1px; }
  .brand__secondary { display: block; font-size: 15.5px; letter-spacing: 6.4px; margin-top: 6px; }

  .license {
    position: absolute; left: 0; right: 0; text-align: center;
    font-family: var(--display); font-weight: 500; font-size: 12px; letter-spacing: 0.5px;
  }
  .banner--stacked .license { top: 300px; }
  .banner--split .license { top: 310px; }

  .phone {
    position: absolute; display: flex; align-items: center; gap: 14px;
    font-family: var(--display); font-weight: 900; font-size: 38px; line-height: 1;
    letter-spacing: 1px;
  }
  .banner--stacked .phone { top: 326px; left: 0; right: 0; justify-content: center; }
  .banner--split .phone { top: 372px; right: 24px; }
  .icon { flex: none; display: block; }
  .icon--phone { width: 30px; height: 30px; }

  .contact {
    position: absolute; display: flex; align-items: center; gap: 9px;
    font-family: var(--body); font-weight: 300; font-size: 19px; line-height: 1;
  }
  .icon--small { width: 15px; height: 15px; }
  .banner--stacked .contact--email { top: 385px; left: 36px; }
  .banner--stacked .contact--web { top: 385px; left: 478px; }
  .banner--split .contact--email { top: 364px; left: 27px; }
  .banner--split .contact--web { top: 392px; left: 27px; }
</style>
</head>
<body>
<main class="sheet">

  <!-- Stacked layout: phone centred, contacts in one row -->
  <section class="banner banner--stacked">
    <svg class="banner__backdrop" viewBox="0 0 851 428" preserveAspectRatio="none" aria-hidden="true">
      <polygon points="0,0 851,0 851,204 425,350 0,204" fill="var(--band-mid)"/>
      <polygon points="0,0 851,0 851,84 425,276 0,84" fill="var(--band-light)"/>
    </svg>
    <h1 class="headline">BUILD WITH THE T-CREW!</h1>
    <div class="brand">
      <span class="brand__mark" aria-hidden="true"></span>
      <p class="brand__name"><span class="brand__primary">THORNWELL</span><span class="brand__secondary">BUILDING COMPANY</span></p>
    </div>
    <p class="license">Lic#5386204</p>
    <p class="phone">
      <svg class="icon icon--phone" viewBox="0 0 30 30" aria-hidden="true">
        <circle cx="15" cy="15" r="13.5" fill="none" stroke="var(--brand-green)" stroke-width="1.5"/>
        <path d="M10.5 8.5l2.6-.6 1.4 3.4-1.7 1.2a8 8 0 0 0 4.2 4.2l1.2-1.7 3.4 1.4-.6 2.6c-6.4.4-11-4.2-10.5-10.5z" fill="var(--brand-green)"/>
      </svg>
      472-318-6095
    </p>
    <p class="contact contact--email">
      <svg class="icon icon--small" viewBox="0 0 15 15" aria-hidden="true">
        <rect x="1" y="3" width="13" height="9" rx="1.5" fill="none" stroke="var(--brand-green)" stroke-width="1.6"/>
        <path d="M2 4.5l5.5 4 5.5-4" fill="none" stroke="var(--brand-green)" stroke-width="1.6"/>
      </svg>
      thornwellbuildingcompany@mailvistra.net
    </p>
    <p class="contact contact--web">
      <svg class="icon icon--small" viewBox="0 0 15 15" aria-hidden="true">
        <circle cx="7.5" cy="7.5" r="6.3" fill="none" stroke="var(--brand-green)" stroke-width="1.6"/>
        <ellipse cx="7.5" cy="7.5" rx="2.6" ry="6.3" fill="none" stroke="var(--brand-green)" stroke-width="1.4"/>
        <path d="M1.2 7.5h12.6" stroke="var(--brand-green)" stroke-width="1.4"/>
      </svg>
      thornwellbuildingcompany.com
    </p>
  </section>

  <!-- Split layout: contacts left, phone right -->
  <section class="banner banner--split">
    <svg class="banner__backdrop" viewBox="0 0 851 428" preserveAspectRatio="none" aria-hidden="true">
      <polygon points="0,0 851,0 851,204 425,350 0,204" fill="var(--band-mid)"/>
      <polygon points="0,0 851,0 851,84 425,276 0,84" fill="var(--band-light)"/>
    </svg>
    <h1 class="headline">BUILD WITH THE T-CREW!</h1>
    <div class="brand">
      <span class="brand__mark" aria-hidden="true"></span>
      <p class="brand__name"><span class="brand__primary">THORNWELL</span><span class="brand__secondary">BUILDING COMPANY</span></p>
    </div>
    <p class="license">Lic#5386204</p>
    <p class="contact contact--email">
      <svg class="icon icon--small" viewBox="0 0 15 15" aria-hidden="true">
        <rect x="1" y="3" width="13" height="9" rx="1.5" fill="none" stroke="var(--brand-green)" stroke-width="1.6"/>
        <path d="M2 4.5l5.5 4 5.5-4" fill="none" stroke="var(--brand-green)" stroke-width="1.6"/>
      </svg>
      thornwellbuildingcompany@mailvistra.net
    </p>
    <p class="contact contact--web">
      <svg class="icon icon--small" viewBox="0 0 15 15" aria-hidden="true">
        <circle cx="7.5" cy="7.5" r="6.3" fill="none" stroke="var(--brand-green)" stroke-width="1.6"/>
        <ellipse cx="7.5" cy="7.5" rx="2.6" ry="6.3" fill="none" stroke="var(--brand-green)" stroke-width="1.4"/>
        <path d="M1.2 7.5h12.6" stroke="var(--brand-green)" stroke-width="1.4"/>
      </svg>
      thornwellbuildingcompany.com
    </p>
    <p class="phone">
      <svg class="icon icon--phone" viewBox="0 0 30 30" aria-hidden="true">
        <circle cx="15" cy="15" r="13.5" fill="none" stroke="var(--brand-green)" stroke-width="1.5"/>
        <path d="M10.5 8.5l2.6-.6 1.4 3.4-1.7 1.2a8 8 0 0 0 4.2 4.2l1.2-1.7 3.4 1.4-.6 2.6c-6.4.4-11-4.2-10.5-10.5z" fill="var(--brand-green)"/>
      </svg>
      472-318-6095
    </p>
  </section>

</main>
</body>
</html>
```